Flyer Design / Authenticity Certificate - Art Work

Looking for a design of a "Authenticity Certificate" - flyer, that will include some basic company info like logo etc, and allow our in house artist to sign and authenticate before it is applied the reverse of one of the paintings we will sell. Linked with our online sales website - "Copper Hollow Canvases", where we recreate one off oil paintings from digital photographs. Our business logo should be incorporated in the design, along with a section for "Artisit Name" "Artisit Signature" "Ref Code"
Updates

Hi.. Sorry I should have added the size we need - please design accordingly to A6. Thanks.

Industry/Entity Type

It Company

Font styles to use
Serif
Script

Colors

Designer to choose colors to be used in the design.

Requirements
Must have
• Company logo
• Area for artist to print and sign
• Area for a reference
Nice to have
• must use the logo, maybe incorporate a "seal" icon, like what was used as a wax seal on older style documents

```html
<!DOCTYPE html>
<html lang="en">
<head>
<meta charset="utf-8">
<title>Certificate of Authenticity – Copper Hollow Canvases</title>
<link rel="stylesheet" href="https://fonts.googleapis.com/css2?family=Open+Sans:wght@400;700&display=swap">
<style>
  :root {
    --page-bg: #e9e9ea;
    --card-bg: #ffffff;
    --ink: #2b2b2b;
    --ink-soft: #333333;
    --brand-grey: #8a8a8a;
    --rule-pink: #d43a93;
    --dot-grey: #b5b5b5;
    --wave-orange: #f59c38;
    --wave-grey: #a9a9a9;
    --wave-blue: #36ace0;
    --wave-red: #e0364e;
  }
  * { margin: 0; padding: 0; box-sizing: border-box; }
  html, body {
    width: 1200px; height: 982px; overflow: hidden;
    background: var(--page-bg);
    font-family: "Open Sans", Arial, sans-serif;
    color: var(--ink);
  }
  .certificate {
    position: absolute; left: 50px; top: 102px;
    width: 1100px; height: 778px;
    background: var(--card-bg);
    overflow: hidden;
    box-shadow: 0 2px 10px rgba(0,0,0,0.12);
  }
  .header-wave { position: absolute; left: 0; top: 0; width: 1100px; height: 270px; }
  .title-main {
    position: absolute; left: 139px; top: 176px;
    font-size: 60px; font-weight: 700; letter-spacing: 0;
    color: var(--ink-soft); line-height: 1;
  }
  .title-sub {
    position: absolute; left: 204px; top: 235px;
    font-size: 31px; font-weight: 700; color: var(--ink-soft); line-height: 1;
  }
  .brand-mark {
    position: absolute; left: 957px; top: 172px;
    width: 84px; height: 84px; margin: -42px 0 0 -42px;
    border-radius: 50%; border: 9px solid var(--ink-soft);
  }
  .brand-name {
    position: absolute; left: 957px; top: 224px; transform: translateX(-50%);
    white-space: nowrap; font-size: 13px; font-weight: 400;
    letter-spacing: 1px; color: var(--brand-grey);
  }
  .artwork-frame { position: absolute; left: 62px; top: 293px; width: 312px; height: 312px; }
  .divider {
    position: absolute; left: 416px; top: 319px; width: 2px; height: 261px;
    background: var(--rule-pink); opacity: 0.7;
  }
  .statement {
    position: absolute; left: 478px; top: 300px; width: 589px;
    font-size: 17.5px; line-height: 26px; text-align: justify; color: #222;
  }
  .sign-line {
    position: absolute; height: 0;
    border-top: 2px dotted var(--rule-pink);
  }
  .field-label {
    position: absolute; transform: translateX(-50%);
    white-space: nowrap; color: var(--ink-soft); line-height: 1;
  }
  .field-label--large { font-size: 21px; }
  .field-label--edition { font-size: 24px; }
  .field-label--small { font-size: 19px; }
  .contact-email {
    position: absolute; left: 549px; top: 747px; transform: translateX(-50%);
    font-size: 17px; color: var(--ink-soft); line-height: 1;
  }
</style>
</head>
<body>
  <main class="certificate">
    <svg class="header-wave" viewBox="0 0 1100 270" preserveAspectRatio="none" role="img" aria-label="Decorative multicolour wave header">
      <defs>
        <linearGradient id="wave-fill" x1="0" y1="0" x2="1" y2="0">
          <stop offset="0" stop-color="var(--wave-orange)"/>
          <stop offset="0.35" stop-color="var(--wave-grey)"/>
          <stop offset="0.7" stop-color="var(--wave-blue)"/>
          <stop offset="1" stop-color="var(--wave-red)"/>
        </linearGradient>
      </defs>
      <path fill="url(#wave-fill)" opacity="0.85" d="M0 0 H1100 C1060 60 960 100 820 125 C640 160 460 140 300 140 C170 145 70 190 0 268 Z"/>
    </svg>

    <h1 class="title-main">CERTIFICATE</h1>
    <p class="title-sub">Of Authenticity</p>

    <div class="brand-mark"></div>
    <p class="brand-name">COPPER HOLLOW CANVASES</p>

    <svg class="artwork-frame" viewBox="0 0 312 312" aria-hidden="true">
      <circle cx="156" cy="156" r="155" fill="none" stroke="var(--dot-grey)" stroke-width="1.3" stroke-dasharray="2 3"/>
    </svg>

    <div class="divider"></div>

    <p class="statement">This certificate of authentication certifies the identification of the art work here beneath, and is offered in an authorised signed and numbered limited edition. No reproduction is permitted without express permission of the artist.</p>

    <div class="sign-line" style="left:540px; top:493px; width:461px;"></div>
    <span class="field-label field-label--large" style="left:770px; top:505px;">Name Of Artist</span>

    <div class="sign-line" style="left:638px; top:595px; width:289px;"></div>
    <span class="field-label field-label--edition" style="left:783px; top:606px;">Art Work Edition</span>

    <div class="sign-line" style="left:52px; top:691px; width:214px;"></div>
    <span class="field-label field-label--small" style="left:159px; top:700px;">Edition No</span>

    <div class="sign-line" style="left:314px; top:691px; width:187px;"></div>
    <span class="field-label field-label--small" style="left:409px; top:700px;">Title</span>

    <div class="sign-line" style="left:552px; top:691px; width:187px;"></div>
    <span class="field-label field-label--small" style="left:628px; top:700px;">Type</span>

    <div class="sign-line" style="left:839px; top:691px; width:210px;"></div>
    <span class="field-label field-label--small" style="left:943px; top:700px;">Artist Signature</span>

    <p class="contact-email">coa@copperhollowcanvases.com</p>
  </main>
</body>
</html>
```